Logo & Visitenkarte für Immobilienunternehmen
Ich bin mit der professionellen und speditiven Umsetzung meiner Vorstellungen sehr zufrieden.
Zielgruppe
Wir sind ein Immobilienunternehmen. Wir sind tätig im Immobilienhandel, der Immobilienvermittlung und der Erstellung von Häusern.
Unsere Zielgruppe sind Personen, die eine Immobilie kaufen oder verkaufen wollen. Personen ab ca. 30 Jahren mit mittlerem bis hohem Kapital bzw. Einkommen
Aufgabenstellung
Das Design soll für Sicherheit, Vertrauen, Seriosität, Professionalität und Hochwertigkeit stehen, da es in der Immobilienbranche oft um sehr viel Geld geht.

```html
<!DOCTYPE html>
<html lang="de">
<head>
<meta charset="utf-8">
<title>Visitenkarte Peter Kolbinger</title>
<link rel="stylesheet" href="https://fonts.googleapis.com/css2?family=Jost:wght@400;500;600&display=swap">
<style>
  :root {
    --page-bg: #f4f4f4;
    --card-light: #ffffff;
    --card-dark: #333333;
    --ink-dark: #1e1e1e;
    --ink-gold: #c9a13c;
    --card-shadow: 0 18px 40px rgba(0, 0, 0, 0.16), 0 2px 6px rgba(0, 0, 0, 0.10);
  }
  * { box-sizing: border-box; margin: 0; padding: 0; }
  html, body {
    width: 1200px;
    height: 675px;
    overflow: hidden;
  }
  body {
    background: var(--page-bg);
    font-family: "Jost", "Futura", sans-serif;
    display: flex;
    align-items: center;
    justify-content: center;
    gap: 60px;
  }
  .business-card {
    width: 510px;
    height: 330px;
    box-shadow: var(--card-shadow);
    display: flex;
    align-items: center;
    justify-content: center;
  }
  .business-card--light { background: var(--card-light); color: var(--ink-dark); }
  .business-card--dark { background: var(--card-dark); color: var(--ink-gold); }
  .contact-block {
    width: 230px;
    margin-left: 60px;
  }
  .contact-name {
    font-weight: 600;
    font-size: 21px;
    letter-spacing: 0.06em;
    text-transform: uppercase;
    line-height: 1.1;
  }
  .contact-role {
    font-size: 11px;
    font-weight: 400;
    letter-spacing: 0.03em;
    margin-top: 3px;
  }
  .contact-address,
  .contact-reach {
    font-size: 14px;
    font-weight: 400;
    line-height: 1.35;
    margin-top: 30px;
  }
  .contact-reach { margin-top: 22px; }
</style>
</head>
<body>
  <section class="business-card business-card--light">
    <div class="contact-block">
      <p class="contact-name">Peter Kolbinger</p>
      <p class="contact-role">Inhaber &amp; Geschäftsführer</p>
      <p class="contact-address">Lindenweg 12<br>6048 Seehalden</p>
      <p class="contact-reach">+41 79 412 58 30<br>info@kolbinger.immobilien.ch</p>
    </div>
  </section>
  <section class="business-card business-card--dark">
    <div class="contact-block">
      <p class="contact-name">Peter Kolbinger</p>
      <p class="contact-role">Inhaber &amp; Geschäftsführer</p>
      <p class="contact-address">Lindenweg 12<br>6048 Seehalden</p>
      <p class="contact-reach">+41 79 412 58 30<br>info@kolbinger.immobilien.ch</p>
    </div>
  </section>
</body>
</html>
```